Accident Law Firm Billboard Bold Easy to See Car Accidents

We need a billboard design that can catch attention in a very crowed Car Accident lawyer market. We wish to feature the phone number (652) 318-4470 as the focus of the Bill Board. We are trying to get the phone number recognized and remembered by drivers. The law firm name is not as crucial to remember.
Basically, It's CAR ACCIDENT? Then (652) 318-4470. We are not married to any specific color scheme but it has to POP and catch attention.
So the Crucial elements are as follows:
1. Phone number (652) 318-4470
2. Words CAR ACCIDENT?
3. Firm Logo in lower portion or where appropriate. Firm Logo to be provided
4. We may want to try a Day Glow orange color, with White and Black added. An example of the color scheme shall be provided.
5. Possible "Catch Phrase" to be used, "It's Time Call 9"
Target Market(s)
Orlando Florida Car Accident victims
Industry/Entity Type
Law Firm
Requirements
Must have
- Easy to see phone number (652) 318-4470
- Catch attention
Nice to have
- I would like to have the sign visible in bright sunlight and it not too hard to immediately know what phone number is for
Should not have
- too many words
- No bold enough
- confusing fonts
- Unclear fonts

```html
<!DOCTYPE html>
<html lang="en">
<head>
<meta charset="utf-8">
<title>Marlowe Law Firm – Car Accident Billboard</title>
<link rel="stylesheet" href="https://fonts.googleapis.com/css2?family=Open+Sans:wght@600;700;800&family=Oswald:wght@500&display=swap">
<style>
  :root {
    --ink: #141414;
    --ink-soft: #242424;
    --orange: #f26a2a;
    --orange-deep: #d9521d;
    --white: #ffffff;
    --page: #e9ecef;
    --car-red: #d8232f;
    --car-dark: #5a1419;
  }
  * { margin: 0; padding: 0; box-sizing: border-box; }
  html, body { width: 1200px; height: 840px; overflow: hidden; background: var(--page); }
  body { display: flex; align-items: center; justify-content: center; font-family: "Open Sans", Arial, sans-serif; }

  .billboard {
    position: relative;
    width: 1120px;
    height: 360px;
    background: radial-gradient(ellipse at 50% 40%, var(--ink-soft), var(--ink) 75%);
    overflow: hidden;
    color: var(--white);
  }

  .accent-panel {
    position: absolute; top: 0; right: 0; width: 90px; height: 100%;
    background: linear-gradient(180deg, var(--orange), var(--orange-deep));
    clip-path: polygon(40% 0, 100% 0, 100% 100%, 0 100%);
  }

  .headline {
    position: absolute; left: 34px; top: 22px;
    font-weight: 800; font-size: 96px; letter-spacing: -1px; line-height: 1;
    text-shadow: 3px 3px 0 rgba(0,0,0,.6);
  }

  .call-band {
    position: absolute; left: 0; top: 124px; height: 66px; width: 680px;
    background: var(--orange);
    clip-path: polygon(0 0, 640px 0, 680px 50%, 640px 100%, 0 100%);
    display: flex; align-items: center; padding-left: 30px; gap: 10px;
  }
  .call-band__label { font-family: "Oswald", "Arial Narrow", sans-serif; font-weight: 500; font-size: 28px; letter-spacing: .2px; }
  .call-band__icon { width: 26px; height: 26px; }
  .call-band__phone { font-weight: 800; font-size: 40px; letter-spacing: .5px; }

  .chevrons { position: absolute; left: 650px; top: 124px; width: 110px; height: 66px; }

  .tagline {
    position: absolute; left: 32px; top: 212px;
    font-weight: 800; font-size: 58px; line-height: 1; letter-spacing: -.5px;
  }
  .website {
    position: absolute; left: 34px; top: 296px;
    font-weight: 600; font-size: 34px; letter-spacing: 2px;
  }

  .firm-name {
    position: absolute; left: 822px; top: 40px;
    font-weight: 800; color: var(--white); line-height: 1;
  }
  .firm-name__main { display: block; font-size: 48px; letter-spacing: .5px; }
  .firm-name__sub { display: block; font-size: 24px; letter-spacing: 1.5px; margin-top: 4px; }

  .vehicle-photo {
    position: absolute; left: 690px; top: 160px; width: 430px; height: 190px;
    background: radial-gradient(ellipse at 60% 50%, var(--car-red) 0%, #b31b25 45%, var(--car-dark) 75%, transparent 78%);
  }
</style>
</head>
<body>
  <main class="billboard">
    <div class="accent-panel"></div>

    <h1 class="headline">CAR ACCIDENT?</h1>

    <div class="call-band">
      <span class="call-band__label">NEED LEGAL ASSISTENCE:</span>
      <svg class="call-band__icon" viewBox="0 0 24 24" fill="none" stroke="#fff" stroke-width="1.6" stroke-linecap="round" stroke-linejoin="round" aria-hidden="true">
        <path d="M5 3h3l2 5-2.5 1.5a11 11 0 0 0 7 7L16 14l5 2v3a2 2 0 0 1-2 2A16 16 0 0 1 3 5a2 2 0 0 1 2-2z"/>
        <path d="M15 3a6 6 0 0 1 6 6M15 7a2 2 0 0 1 2 2"/>
      </svg>
      <span class="call-band__phone">(652) 318-4470</span>
    </div>

    <svg class="chevrons" viewBox="0 0 110 66" aria-hidden="true">
      <polygon points="22,0 50,0 84,33 50,66 22,66 56,33" fill="#f26a2a"/>
      <polygon points="56,0 76,0 110,33 76,66 56,66 90,33" fill="#f26a2a"/>
    </svg>

    <p class="tagline">"IT'S TIME CALL 9"</p>
    <p class="website">www.website.com</p>

    <div class="firm-name">
      <span class="firm-name__main">MARLOWE</span>
      <span class="firm-name__sub">LAW FIRM P.C.</span>
    </div>

    <div class="vehicle-photo" role="img" aria-label="Photo of a red sports car with a crushed front end after a collision"></div>
  </main>
</body>
</html>
```